business card for LWR pty ltd

We require a business card that stands out . I have included our company flyer and would like the services listed to be put on the card so when we Give out the cards to customers they have an idea of services we provide. need the winning design to be in editable photo shop format, editable iMac pages format or editable windows publisher format, so that I can enter in names, email addresses, phone numbers etc myself. I have included a pdf documents of info / items needed on the card to use as reference please.
Updates

need more submissions

Need extra days to review

Sick

Target Market(s)

new customers

Contact Information for Business Card

details are on attached business card requirements file

Requirements
Must have
• I have attached a list of must haves

```html
<!DOCTYPE html>
<html lang="en">
<head>
<meta charset="utf-8">
<title>LWR pty ltd – Business Card</title>
<link rel="stylesheet" href="https://fonts.googleapis.com/css2?family=Saira+Semi+Condensed:wght@500;600;700&display=swap">
<style>
  :root {
    --page: #ffffff;
    --card: #050505;
    --band-dark: #0d0a08;
    --gold: #a97b3b;
    --text: #ffffff;
    --muted: #a9a9a9;
    --logo: #bdbdbd;
    --icon-ink: #0a0a0a;
  }
  * { box-sizing: border-box; margin: 0; padding: 0; }
  html, body {
    width: 1141px; height: 1200px; overflow: hidden;
    background: var(--page);
    font-family: "Saira Semi Condensed", "Arial Narrow", sans-serif;
  }
  .card {
    position: absolute; left: 137px; width: 855px; height: 487px;
    border-radius: 26px; overflow: hidden; background: var(--card);
  }
  .card--front { top: 88px; }
  .card--back { top: 618px; background: radial-gradient(ellipse at 50% 40%, #151515 0%, #070707 70%); }

  .front__texture {
    position: absolute; left: 0; top: 0; width: 855px; height: 318px;
    background: radial-gradient(ellipse at 50% 30%, #3a3a3a 0%, #1c1c1c 45%, #0b0b0b 100%);
  }
  .front__bands { position: absolute; left: 0; top: 0; }
  .front__logo {
    position: absolute; left: 0; top: 64px; width: 855px; text-align: center;
    font-weight: 700; font-size: 150px; line-height: 1; letter-spacing: 4px;
    color: var(--logo);
  }
  .front__identity { position: absolute; left: 91px; top: 380px; color: var(--text); white-space: nowrap; }
  .front__company { font-weight: 700; font-size: 29px; line-height: 34px; }
  .front__person { font-weight: 700; font-size: 25px; line-height: 34px; margin-top: 2px; }
  .front__role { color: var(--muted); }

  .contact-list { position: absolute; left: 472px; top: 362px; list-style: none; }
  .contact-list li {
    display: flex; align-items: center; height: 27px; white-space: nowrap;
    font-weight: 500; font-size: 15.5px; color: var(--muted);
  }
  .contact-list svg { width: 15px; height: 15px; margin-right: 18px; fill: var(--gold); flex: none; }

  .back__band { position: absolute; left: 0; top: 0; }
  .service-list { position: absolute; top: 77px; list-style: none; }
  .service-list--left { left: 132px; }
  .service-list--right { left: 448px; }
  .service-list li {
    display: flex; align-items: center; height: 27px; white-space: nowrap;
    font-weight: 500; font-size: 15.8px; color: var(--text);
  }
  .tick { width: 15px; height: 15px; margin-right: 12px; flex: none; }
  .back__photo {
    position: absolute; left: 112px; top: 262px; width: 725px; height: 212px;
    border-radius: 6px;
    background: linear-gradient(90deg, rgba(190,180,165,0.25) 0%, rgba(200,190,175,0.55) 45%, rgba(30,35,45,0.9) 75%, rgba(160,150,130,0.5) 100%);
  }
</style>
</head>
<body>
  <section class="card card--front">
    <div class="front__texture" role="img" aria-label="Dark metallic mesh texture behind the company name"></div>
    <svg class="front__bands" width="855" height="487" viewBox="0 0 855 487" aria-hidden="true">
      <polygon points="182,318 855,318 855,338 182,338" fill="var(--band-dark)"/>
      <polygon points="214,301 855,301 855,317 198,317" fill="var(--gold)"/>
    </svg>
    <div class="front__logo">LWR</div>

    <div class="front__identity">
      <p class="front__company">LWR pty ltd</p>
      <p class="front__person">DANIEL HARTLEY <span class="front__role">(Director)</span></p>
    </div>

    <ul class="contact-list">
      <li><svg viewBox="0 0 16 16"><path d="M8 1a5 5 0 0 0-5 5c0 3.6 5 9 5 9s5-5.4 5-9a5 5 0 0 0-5-5zm0 7a2 2 0 1 1 0-4 2 2 0 0 1 0 4z"/></svg>Depot: Lot 444 example address Australia</li>
      <li><svg viewBox="0 0 16 16"><path d="M1 4h14v1.2L8 9.5 1 5.2z"/><path d="M1 6.6l7 4.3 7-4.3V13H1z"/></svg>Email: email@redplainhaulage.com.au</li>
      <li><svg viewBox="0 0 16 16"><path d="M3.6 1.5l2.3 2.8-1.3 1.7c.9 2 2.5 3.6 4.4 4.5l1.7-1.3 2.8 2.3-1.4 2.3C7 13.4 2.6 9 1.3 2.9z"/></svg>Phone: 000 444 000</li>
      <li><svg viewBox="0 0 16 16"><circle cx="8" cy="8" r="7"/><path d="M5 3.5c1.5.5 1.5 2 3 2.5s1 2-1 2.5-1 2.5 0 4M10.5 9.5c1 .5 2 0 3 .5" stroke="#050505" stroke-width="1.3" fill="none"/></svg>Website: www.websiteaddress.com</li>
    </ul>
  </section>

  <section class="card card--back">
    <svg class="back__band" width="855" height="12" viewBox="0 0 855 12" aria-hidden="true">
      <polygon points="0,0 654,0 644,10 0,10" fill="var(--gold)"/>
    </svg>

    <ul class="service-list service-list--left">
      <li><svg class="tick" viewBox="0 0 16 16"><circle cx="8" cy="8" r="8" fill="var(--gold)"/><path d="M4.5 8.2l2.3 2.3 4.7-4.7" stroke="var(--icon-ink)" stroke-width="2" fill="none"/></svg>Over size loads/Hot Shot Loads</li>
      <li><svg class="tick" viewBox="0 0 16 16"><circle cx="8" cy="8" r="8" fill="var(--gold)"/><path d="M4.5 8.2l2.3 2.3 4.7-4.7" stroke="var(--icon-ink)" stroke-width="2" fill="none"/></svg>Heavy Vehicle Recovery services</li>
      <li><svg class="tick" viewBox="0 0 16 16"><circle cx="8" cy="8" r="8" fill="var(--gold)"/><path d="M4.5 8.2l2.3 2.3 4.7-4.7" stroke="var(--icon-ink)" stroke-width="2" fill="none"/></svg>Potable Water Deliveries</li>
      <li><svg class="tick" viewBox="0 0 16 16"><circle cx="8" cy="8" r="8" fill="var(--gold)"/><path d="M4.5 8.2l2.3 2.3 4.7-4.7" stroke="var(--icon-ink)" stroke-width="2" fill="none"/></svg>Road Building/Maintenance</li>
      <li><svg class="tick" viewBox="0 0 16 16"><circle cx="8" cy="8" r="8" fill="var(--gold)"/><path d="M4.5 8.2l2.3 2.3 4.7-4.7" stroke="var(--icon-ink)" stroke-width="2" fill="none"/></svg>Earthworks</li>
      <li><svg class="tick" viewBox="0 0 16 16"><circle cx="8" cy="8" r="8" fill="var(--gold)"/><path d="M4.5 8.2l2.3 2.3 4.7-4.7" stroke="var(--icon-ink)" stroke-width="2" fill="none"/></svg>Sand &amp; Metal Supply &amp; Cartage</li>
    </ul>

    <ul class="service-list service-list--right">
      <li><svg class="tick" viewBox="0 0 16 16"><circle cx="8" cy="8" r="8" fill="var(--gold)"/><path d="M4.5 8.2l2.3 2.3 4.7-4.7" stroke="var(--icon-ink)" stroke-width="2" fill="none"/></svg>Road Train Tippers</li>
      <li><svg class="tick" viewBox="0 0 16 16"><circle cx="8" cy="8" r="8" fill="var(--gold)"/><path d="M4.5 8.2l2.3 2.3 4.7-4.7" stroke="var(--icon-ink)" stroke-width="2" fill="none"/></svg>Road Train Tankers</li>
      <li><svg class="tick" viewBox="0 0 16 16"><circle cx="8" cy="8" r="8" fill="var(--gold)"/><path d="M4.5 8.2l2.3 2.3 4.7-4.7" stroke="var(--icon-ink)" stroke-width="2" fill="none"/></svg>Road Train Flat Tops</li>
      <li><svg class="tick" viewBox="0 0 16 16"><circle cx="8" cy="8" r="8" fill="var(--gold)"/><path d="M4.5 8.2l2.3 2.3 4.7-4.7" stroke="var(--icon-ink)" stroke-width="2" fill="none"/></svg>Drop Deck Trailers</li>
      <li><svg class="tick" viewBox="0 0 16 16"><circle cx="8" cy="8" r="8" fill="var(--gold)"/><path d="M4.5 8.2l2.3 2.3 4.7-4.7" stroke="var(--icon-ink)" stroke-width="2" fill="none"/></svg>Mine site accredited equipment &amp; Operators</li>
    </ul>

    <div class="back__photo" role="img" aria-label="Photo of a road train truck hauling white water tanker trailers"></div>
  </section>
</body>
</html>
```